pop up booking component and calendar re-design

we have a calander view where a parent cant reserve a day
you can click on please redesign the calander / voucher and pop up.

the dropdowns in pop up can be buttons
the dots on the calander indicate if there is space or not

when booking a day you can select a voucher

we used KIVO as inspiration, you are welcome to look at it as well.. screenshots attached

please ask questions if you have any

```html
<!DOCTYPE html>
<html lang="en">
<head>
<meta charset="utf-8">
<title>Book day</title>
<link rel="stylesheet" href="https://fonts.googleapis.com/css2?family=Roboto:wght@300;400;500;700&display=swap">
<style>
:root{
  --green:#0db14b;
  --green-dark:#0a9e42;
  --ink:#2b2b2b;
  --muted:#9a9a9a;
  --line:#ececec;
  --card:#efefef;
  --card-band:#e6e6e6;
  --chip:#f0f0f0;
  --page:#ffffff;
  --tray:#f4f4f4;
  --white:#ffffff;
}
*{margin:0;padding:0;box-sizing:border-box}
html,body{width:1200px;height:2596px;overflow:hidden;background:var(--page)}
body{font-family:"Roboto",sans-serif;color:var(--ink);position:relative}
.abs{position:absolute}

.status-time{left:48px;top:52px;font-size:52px;font-weight:500;color:#bdbdbd}
.status-icons{right:36px;top:56px}

.day-card{top:160px;width:440px;height:492px;background:var(--card);color:var(--ink);overflow:hidden}
.day-card.is-selected{background:var(--green);color:var(--white)}
.day-card .date{position:absolute;left:24px;top:60px;font-size:74px;font-weight:400;line-height:1}
.day-card .weekday{position:absolute;left:24px;top:144px;font-size:34px;opacity:.7}
.day-card .group{position:absolute;left:24px;top:236px;font-size:40px;white-space:nowrap}
.day-card .fee{position:absolute;left:24px;top:290px;font-size:40px}
.day-card .band{position:absolute;left:0;right:0;bottom:0;height:76px;background:var(--card-band);font-size:32px;padding:28px 24px 0;opacity:1;color:var(--muted)}
.day-card.is-selected .band{background:var(--green-dark);color:rgba(255,255,255,.75)}

.title{left:80px;top:750px;font-size:70px;font-weight:400}
.title-date{right:60px;top:774px;font-size:40px;color:var(--muted)}

.row-icon{left:80px}
.row-label{left:192px;font-size:44px}
.row-sub{left:192px;font-size:36px;color:var(--muted)}
.divider{left:192px;right:60px;height:3px;background:var(--line)}
.chevron{right:64px}

.bso{right:208px;top:976px;font-size:44px;font-weight:500}
.toggle{left:1016px;top:976px;width:120px;height:68px;border-radius:34px;background:var(--green)}
.toggle::after{content:"";position:absolute;right:8px;top:8px;width:52px;height:52px;border-radius:50%;background:var(--white)}

.segments{left:192px;top:1608px;display:flex;gap:18px}
.segment{width:174px;height:76px;border-radius:6px;background:var(--chip);color:#c0c0c0;font-size:40px;display:flex;align-items:center;justify-content:center}
.segment.is-active{background:var(--green);color:var(--white)}

.tray{left:0;right:0;top:1840px;bottom:0;background:var(--tray)}
.summary{left:48px;top:1900px;width:1104px;height:652px;background:var(--white);box-shadow:0 6px 30px rgba(0,0,0,.08)}
.summary-col{top:52px;width:368px;text-align:center}
.summary-col .value{font-size:40px;color:var(--muted);height:56px}
.summary-col .label{font-size:38px;margin-top:12px}
.vsep{top:48px;width:3px;height:116px;background:var(--line)}
.hsep{left:52px;right:52px;top:236px;height:3px;background:var(--line)}
.total{left:0;right:0;top:300px;text-align:center}
.total .amount{font-size:44px;font-weight:700}
.total .label{font-size:38px;color:var(--ink);margin-top:14px}
.btn{top:476px;width:476px;height:140px;border-radius:8px;font-size:46px;font-weight:500;display:flex;align-items:center;justify-content:center}
.btn-cancel{left:56px;background:#e7e7e7;color:var(--ink)}
.btn-confirm{left:568px;background:var(--green);color:var(--white)}
</style>
</head>
<body>

<div class="abs status-time">9:41</div>
<svg class="abs status-icons" width="180" height="40" viewBox="0 0 180 40" aria-hidden="true">
  <g fill="#bdbdbd">
    <rect x="0" y="26" width="9" height="12" rx="2"/><rect x="14" y="19" width="9" height="19" rx="2"/>
    <rect x="28" y="12" width="9" height="26" rx="2"/><rect x="42" y="4" width="9" height="34" rx="2"/>
    <path d="M84 36l-7-8a11 11 0 0 1 14 0z"/>
    <path d="M70 20a20 20 0 0 1 28 0l-4 4a14 14 0 0 0-20 0z"/>
    <path d="M63 13a30 30 0 0 1 42 0l-4 4a24 24 0 0 0-34 0z"/>
    <rect x="118" y="8" width="50" height="26" rx="6" fill="none" stroke="#bdbdbd" stroke-width="3"/>
    <rect x="122" y="12" width="42" height="18" rx="3"/><rect x="171" y="16" width="4" height="10" rx="2"/>
  </g>
</svg>

<div class="abs day-card" style="left:48px">
  <div class="date">17</div><div class="weekday">Fri</div>
  <div class="group">RBW-3-Penguins</div><div class="fee">$100.00</div>
  <div class="band">07:30 - 18:30</div>
</div>
<div class="abs day-card is-selected" style="left:540px">
  <div class="date">18</div><div class="weekday">Fri</div>
  <div class="group">RBW-3-Penguins</div><div class="fee">$100.00</div>
  <div class="band">07:30 - 18:30</div>
</div>
<div class="abs day-card" style="left:1032px">
  <div class="date">19</div><div class="weekday">Fri</div>
  <div class="group">RBW-3-Penguins</div><div class="fee">$100.00</div>
  <div class="band">07:30 - 18:30</div>
</div>

<h1 class="abs title">Book day</h1>
<div class="abs title-date">01 Sep 2019</div>

<svg class="abs row-icon" style="top:968px" width="48" height="48" viewBox="0 0 48 48" aria-hidden="true">
  <g fill="#c4c4c4"><rect x="4" y="4" width="18" height="18"/><rect x="4" y="26" width="18" height="18"/><rect x="26" y="26" width="18" height="18"/></g>
</svg>
<div class="abs row-label" style="top:956px">Availability</div>
<div class="abs row-sub" style="top:1014px">1m/1a left</div>
<div class="abs bso">BSO</div>
<div class="abs toggle"></div>
<div class="abs divider" style="top:1124px"></div>

<svg class="abs row-icon" style="top:1174px" width="44" height="56" viewBox="0 0 44 56" aria-hidden="true">
  <path d="M22 2a18 18 0 0 0-18 18c0 14 18 34 18 34s18-20 18-34A18 18 0 0 0 22 2zm0 25a7 7 0 1 1 0-14 7 7 0 0 1 0 14z" fill="#c4c4c4"/>
</svg>
<div class="abs row-label" style="top:1164px">Location</div>
<div class="abs row-sub" style="top:1222px">RBW</div>
<svg class="abs chevron" style="top:1200px" width="24" height="36" viewBox="0 0 24 36" aria-hidden="true"><path d="M4 4l14 14L4 32" fill="none" stroke="var(--green)" stroke-width="5"/></svg>
<div class="abs divider" style="top:1326px"></div>

<svg class="abs row-icon" style="top:1384px" width="48" height="48" viewBox="0 0 48 48" aria-hidden="true">
  <g fill="#c4c4c4"><circle cx="24" cy="14" r="11"/><path d="M2 46c0-12 10-18 22-18s22 6 22 18z"/></g>
</svg>
<div class="abs row-label" style="top:1374px">Group</div>
<div class="abs row-sub" style="top:1432px">3-Penguins</div>
<svg class="abs chevron" style="top:1410px" width="24" height="36" viewBox="0 0 24 36" aria-hidden="true"><path d="M4 4l14 14L4 32" fill="none" stroke="var(--green)" stroke-width="5"/></svg>
<div class="abs divider" style="top:1538px"></div>

<svg class="abs row-icon" style="top:1622px" width="48" height="48" viewBox="0 0 48 48" aria-hidden="true">
  <circle cx="24" cy="24" r="22" fill="#c4c4c4"/><path d="M24 11v14h10" fill="none" stroke="#fff" stroke-width="4"/>
</svg>
<div class="abs segments">
  <div class="segment is-active">Full</div>
  <div class="segment">AM</div>
  <div class="segment">PM</div>
  <div class="segment">Flex</div>
  <div class="segment">Try</div>
</div>

<div class="abs tray"></div>
<section class="abs summary">
  <div class="abs summary-col" style="left:0">
    <div class="value">$100.00</div><div class="label">Price</div>
  </div>
  <div class="abs vsep" style="left:340px"></div>
  <div class="abs summary-col" style="left:368px">
    <div class="value">
      <svg width="130" height="56" viewBox="0 0 130 56" aria-hidden="true">
        <path d="M24 12h50v10a6 6 0 0 0 0 12v10H24V34a6 6 0 0 0 0-12z" fill="none" stroke="#555" stroke-width="3"/>
        <path d="M38 22h22M38 28h22M38 34h14" stroke="#555" stroke-width="3"/>
        <circle cx="100" cy="28" r="22" fill="var(--green)"/>
        <path d="M89 28l8 8 14-15" fill="none" stroke="#fff" stroke-width="5"/>
      </svg>
    </div>
    <div class="label">Voucher</div>
  </div>
  <div class="abs vsep" style="left:732px"></div>
  <div class="abs summary-col" style="left:736px">
    <div class="value">
      <svg width="64" height="56" viewBox="0 0 64 56" aria-hidden="true">
        <g fill="none" stroke="#999" stroke-width="3"><circle cx="10" cy="28" r="6"/><circle cx="32" cy="28" r="6"/><circle cx="54" cy="28" r="6"/></g>
      </svg>
    </div>
    <div class="label">Options</div>
  </div>
  <div class="abs hsep"></div>
  <div class="abs total">
    <div class="amount">$100.00</div>
    <div class="label">Total</div>
  </div>
  <div class="abs btn btn-cancel">Cancel Booking</div>
  <div class="abs btn btn-confirm">Confirm Booking</div>
</section>

</body>
</html>
```